Email Signature

We are looking for creative email signature for our company. Please find attached the logo of our company for your reference. now we understand there isn't much can be done with email signature but we are looking for out of the box designs. Nothing specific in mind

Please insert fake numbers, website and/or address, etc just to showcase the designs. once the design is chosen we will provide the actual details.
Updates

Dear All,

We wouldlike to extend our apology for not being able to provide feedbacks to everysingle design. We were extremely busy and we have multiple contests opensimultaneously which makes the process harder. However, thank you all for theefforts you have put into this contest. We have received anoverwhelming quality responses & it has been a very difficult task tochoose just one, we easily Loved at least several designs...

Thanksagain for participating, we wish you all success in your design ventures.

Kindregards,

HLW Team

Industry/Entity Type

It Company

```html
<!DOCTYPE html>
<html lang="en">
<head>
<meta charset="utf-8">
<title>Harbor Lantern Works – Email Signature</title>
<link rel="stylesheet" href="https://fonts.googleapis.com/css2?family=Open+Sans:wght@400;800&family=Dancing+Script:wght@700&display=swap">
<style>
  :root {
    --brand-blue: #1a86d8;
    --brand-green: #8cc63f;
    --frame-grey: #6d6e71;
    --ink: #111111;
    --paper: #ffffff;
  }
  html, body {
    margin: 0;
    padding: 0;
    width: 1200px;
    height: 856px;
    overflow: hidden;
    background: var(--paper);
  }
  .canvas {
    position: relative;
    width: 1200px;
    height: 856px;
    font-family: "Open Sans", Arial, sans-serif;
  }
  .signature-frame {
    position: absolute;
    left: 0;
    top: 0;
  }
  .brand-mark {
    position: absolute;
    left: 92px;
    top: 208px;
    display: flex;
    align-items: center;
    gap: 14px;
  }
  .brand-dot {
    width: 26px;
    height: 26px;
    border-radius: 50%;
    background: var(--brand-blue);
  }
  .brand-name {
    font-weight: 800;
    font-size: 40px;
    line-height: 1;
    color: var(--brand-blue);
    letter-spacing: -0.5px;
  }
  .contact {
    position: absolute;
    left: 679px;
    top: 180px;
    color: var(--ink);
  }
  .contact-name {
    margin: 0;
    font-family: "Dancing Script", cursive;
    font-weight: 700;
    font-size: 23px;
    line-height: 28px;
    color: var(--brand-green);
  }
  .contact-role {
    margin: 0 0 22px;
    font-size: 15.5px;
    line-height: 22px;
  }
  .contact-line {
    margin: 0;
    font-size: 15.5px;
    line-height: 21px;
  }
  .web-link {
    position: absolute;
    left: 679px;
    top: 306px;
    margin: 0;
    font-size: 19px;
    line-height: 26px;
    color: var(--brand-blue);
  }
</style>
</head>
<body>
  <main class="canvas">
    <svg class="signature-frame" width="1200" height="856" viewBox="0 0 1200 856" aria-hidden="true">
      <rect x="596" y="174" width="476" height="128" rx="18" ry="18"
            fill="none" stroke="var(--frame-grey)" stroke-width="2.5"/>
    </svg>

    <div class="brand-mark">
      <span class="brand-dot"></span>
      <span class="brand-name">Harbor Lantern Works</span>
    </div>

    <section class="contact">
      <p class="contact-name">Nadia Corwell</p>
      <p class="contact-role">Business Owner</p>
      <p class="contact-line">4410 Cedar Quay, Suite 310 Dubai</p>
      <p class="contact-line">Office: 555-014-2288 Fax: 555-014-2288</p>
    </section>

    <p class="web-link">Visit our web site: www.harborlantern.com</p>
  </main>
</body>
</html>
```